Pawsome Trails business card

I need a business card design for a dog training company in Toronto called Pawsome Trails. My training is unique, outdoor training that helps people create a better bond with their dog through communication and understanding their dog's true nature. I do not use treats - but communication and praise for the dog.

I help people create a better life for them and their dog. From puppy training right through to seniors, I offer both group classes called Curbside Calm Program as well as in-home private sessions.

I believe that having a dog is a lifestyle, so I encourage clients to incorporate their dog into their active life. Outdoor activities such as hiking, mental stimulation, proper care and healthy food for their dog are all keys to a healthy and happy dog.

I would like a fresh and modern look that works with my logo. I would like to convey fun, confidence and happiness.

My services are premium services. I am a Certified Dog Trainer, and offer value for money, but my prices are higher than other trainers.
Updates

Thank you to everyone who submitted designs! I'm so impressed with the level of creativity and the options that you all have given me. It will be a difficult choice for sure. As this was my first experience with Sketch Bazaar - it has been a great one.

marla.

Industry/Entity Type

Communication

Requirements
Must have
• Marla Quinby, CTE
Certified Trainer Educator
marla@pawsometrails.ca
647-555-0183
pawsometrails.ca

Prefer a double sided card.
Must have Pawsome Trails logo. File attached. I do have a stroke logo for a dark background as well.

Must only use the fonts and colours as outlined in my brand guidelines, which are attached.
Should not have
• no cheesy pet images
do not use the tongue as an element outside of the logo
minimize the use of pink - can be used as an accent colour but should not be a main colour

```html
<!DOCTYPE html>
<html lang="en">
<head>
<meta charset="utf-8">
<title>Pawsome Trails business card</title>
<link rel="stylesheet" href="https://fonts.googleapis.com/css2?family=Cookie&family=Jost:wght@400;500;800&display=swap">
<style>
  :root {
    --page: #ececec;
    --paper: #ffffff;
    --charcoal: #554e4d;
    --charcoal-soft: #726766;
    --lime: #a5bf3a;
  }
  * { margin: 0; padding: 0; box-sizing: border-box; }
  html, body {
    width: 1200px; height: 1023px; overflow: hidden;
    background: var(--page);
    font-family: "Jost", "Futura", sans-serif;
  }
  .card {
    position: absolute;
    top: 148px;
    width: 409px; height: 714px;
    border-radius: 36px;
    overflow: hidden;
  }
  .card--front { left: 141px; background: var(--paper); }
  .card--back { left: 658px; background: var(--charcoal); }

  .brand-name {
    position: absolute; left: 40px; top: 66px;
    font-weight: 800; font-size: 64px; line-height: 0.95;
    color: var(--charcoal); letter-spacing: -1px;
  }
  .person { position: absolute; left: 40px; top: 374px; }
  .person__name { font-size: 27px; font-weight: 500; color: var(--charcoal); }
  .person__title {
    font-size: 17px; font-weight: 500; color: var(--lime);
    text-transform: uppercase; margin-top: 2px;
  }
  .contact { position: absolute; left: 40px; top: 576px; list-style: none; }
  .contact li { font-size: 22px; color: var(--charcoal); line-height: 30px; }
  .contact__key { display: inline-block; width: 21px; color: var(--lime); }

  .brand-watermark {
    position: absolute; left: -6px; top: 228px;
    font-weight: 800; font-size: 118px; line-height: 0.9;
    color: var(--charcoal-soft); letter-spacing: -3px; white-space: nowrap;
  }
  .seal { position: absolute; left: 193px; top: 133px; }
  .tagline {
    position: absolute; left: 0; right: 0; top: 568px;
    text-align: center; font-family: "Cookie", "Brush Script MT", cursive;
    font-size: 48px; line-height: 52px; color: var(--lime);
  }
</style>
</head>
<body>
  <section class="card card--front">
    <div class="brand-name">Pawsome<br>Trails</div>
    <div class="person">
      <div class="person__name">Marla Quinby, CTE</div>
      <div class="person__title">Certified Trainer Educator</div>
    </div>
    <ul class="contact">
      <li><span class="contact__key">e</span>marla@pawsometrails.ca</li>
      <li><span class="contact__key">t</span>647-555-0183</li>
      <li><span class="contact__key">w</span>pawsometrails.ca</li>
    </ul>
  </section>

  <section class="card card--back">
    <div class="brand-watermark">Pawsome<br>Trails</div>
    <svg class="seal" width="184" height="184" viewBox="0 0 184 184" role="img" aria-label="Certification seal">
      <circle cx="92" cy="92" r="89" fill="var(--charcoal)" stroke="var(--lime)" stroke-width="3"/>
      <circle cx="92" cy="92" r="62" fill="none" stroke="var(--lime)" stroke-width="2"/>
      <circle cx="92" cy="92" r="36" fill="var(--lime)"/>
    </svg>
    <p class="tagline">Bring out the best<br>in your dog</p>
  </section>
</body>
</html>
```